Harrowgate Estates Business Card for Apartment Buildings

Create business cards for resident managers who run apartment buildings. The audience is the public who are searching for apartment rentals, and current residents who live at the apartment building. Key design element will be incorporating the company logo, however, the logo cannot dominate. The building name and manager name are more important than the logo. Current business card design leaves little room for copy, so we may need to reduce the size on the current card to allow for more space for copy.

Target Market(s)

Adults 18-65 years of age, who are looking for an apartment rental, plus current residents who live at our apartment buildings.

Industry/Entity Type

Property Management

Contact Information for Business Card

A major design element will be use of the company logo. Important property and manager contact information must be part of the design. The size of the logo will need to be reduced to make room for building and manager contact copy.

Font styles to use
Sans Serif

Colors
3176b5
000000
959595
ffffff

Requirements
Must have
• 1) Incorporate the company logo.
• 2) Use the company colors (dark blue, black/grey, over white).
• 3) FEATURE THE BUILDING NAME
• 4) FEATURE THE MANAGER NAME
• 5) The company name is less important than BUILDING and MANAGER
• 6) Manager contact information
• **SEE ATTACHED CREATIVE BRIEF**
Nice to have
• 1) Back of card logo watermark
• 2) Ability to write notes on back of carfd
Should not have
• Avoid letting the company logo dominate the card, the building name and manager are more important than the company logo.

```html
<!DOCTYPE html>
<html lang="en">
<head>
<meta charset="utf-8">
<title>Harrowgate Estates Business Card</title>
<link rel="stylesheet" href="https://fonts.googleapis.com/css2?family=Roboto:wght@400;500&family=Oswald:wght@600&display=swap">
<style>
  :root {
    --brand-blue: #3176b5;
    --ink: #1a1a1a;
    --grey: #959595;
    --paper: #ffffff;
    --backdrop: #e4e5e6;
  }
  * { box-sizing: border-box; margin: 0; padding: 0; }
  html, body { width: 1200px; height: 726px; overflow: hidden; }
  body {
    background: var(--backdrop);
    font-family: "Roboto", Arial, sans-serif;
    color: var(--ink);
    position: relative;
  }
  .card {
    position: absolute;
    top: 208px;
    width: 540px;
    height: 310px;
    background: var(--paper);
    box-shadow: 0 6px 18px rgba(0,0,0,0.12);
  }
  .card--front { left: 40px; }
  .card--back { left: 620px; }

  /* Front: company name kept modest so it does not dominate */
  .brand {
    position: absolute;
    top: 118px;
    left: 0; right: 0;
    display: flex;
    justify-content: center;
    align-items: center;
    gap: 10px;
  }
  .brand__mark {
    width: 22px; height: 22px;
    background: var(--brand-blue);
  }
  .brand__name {
    font-family: "Roboto", Arial, sans-serif;
    font-weight: 500;
    font-size: 26px;
    letter-spacing: 1px;
    color: var(--brand-blue);
    text-transform: uppercase;
  }
  .front__web {
    position: absolute;
    bottom: 48px;
    left: 0; right: 0;
    text-align: center;
    font-size: 14px;
    color: var(--ink);
  }
  .front__web span { color: var(--brand-blue); }

  /* Back: manager name is the lead element */
  .manager {
    position: absolute;
    left: 40px;
    top: 108px;
  }
  .manager__name {
    font-family: "Oswald", "Arial Narrow", sans-serif;
    font-weight: 600;
    font-size: 36px;
    line-height: 1;
    color: var(--brand-blue);
    text-transform: uppercase;
  }
  .manager__title {
    margin-top: 6px;
    font-size: 20px;
    color: var(--ink);
  }
  .contacts {
    position: absolute;
    left: 300px;
    top: 80px;
    list-style: none;
    font-size: 14px;
    line-height: 21px;
  }
  .contacts li { display: flex; align-items: center; gap: 10px; white-space: nowrap; }
  .contacts svg { width: 13px; height: 13px; flex: none; }
  .contacts .accent { color: var(--brand-blue); }
  .back__address {
    position: absolute;
    left: 40px; right: 40px;
    top: 222px;
    text-align: center;
    font-size: 15px;
    color: var(--ink);
  }
  .back__rule {
    position: absolute;
    left: 40px; right: 40px;
    top: 254px;
    height: 1.5px;
    background: var(--brand-blue);
  }
</style>
</head>
<body>
  <section class="card card--front" aria-label="Card front">
    <div class="brand">
      <div class="brand__mark"></div>
      <div class="brand__name">Harrowgate Estates</div>
    </div>
    <p class="front__web">www.<span>harrowgateestates</span>.us</p>
  </section>

  <section class="card card--back" aria-label="Card back">
    <div class="manager">
      <h1 class="manager__name">Dana Whitfield</h1>
      <p class="manager__title">Property Manager</p>
    </div>
    <ul class="contacts">
      <li>
        <svg viewBox="0 0 16 16" aria-hidden="true"><circle cx="8" cy="8" r="7" fill="none" stroke="#1a1a1a" stroke-width="1.4"/><path d="M5.5 4.5l1.5 0 .6 2-1 .8a5 5 0 0 0 2.1 2.1l.8-1 2 .6v1.5c-3.5.5-6.5-2.5-6-6z" fill="#1a1a1a"/></svg>
        555-302-4417
      </li>
      <li>
        <svg viewBox="0 0 16 16" aria-hidden="true"><rect x="4" y="1.5" width="8" height="4" fill="#1a1a1a"/><rect x="1.5" y="6" width="13" height="6" rx="1" fill="#1a1a1a"/><rect x="4" y="10" width="8" height="4.5" fill="#fff" stroke="#1a1a1a" stroke-width="1"/></svg>
        555-302-4480
      </li>
      <li>
        <svg viewBox="0 0 16 16" aria-hidden="true"><rect x="1.5" y="3.5" width="13" height="9" fill="none" stroke="#1a1a1a" stroke-width="1.4"/><path d="M1.5 3.5L8 9l6.5-5.5" fill="none" stroke="#1a1a1a" stroke-width="1.4"/></svg>
        dana@harrowgateestates.us
      </li>
      <li>
        <svg viewBox="0 0 16 16" aria-hidden="true"><circle cx="8" cy="8" r="6.5" fill="none" stroke="#1a1a1a" stroke-width="1.4"/><ellipse cx="8" cy="8" rx="2.8" ry="6.5" fill="none" stroke="#1a1a1a" stroke-width="1.2"/><path d="M1.5 8h13" stroke="#1a1a1a" stroke-width="1.2"/></svg>
        <span>www.<span class="accent">harrowgateestates</span>.us</span>
      </li>
    </ul>
    <p class="back__address">2870 Alder Creek Road #B210 Fairview, CA 90471</p>
    <div class="back__rule"></div>
  </section>
</body>
</html>
```